Vorex Malden Car Wrap

Vehicle: 2025 Vorex Malden (Compact SUV) Style: Luxury, Earthy, Minimalist, Calm Coverage: Full Wrap including the roof (car is silver which does not tie in with the branding)

The Visual Concept: "The Earthy Reset"
Primary Base Color: A deep, matte earthy brown (sampled from the Tidal Housekeep Co. logo). We want to avoid high-gloss "commercial" finishes. A satin finish will give that luxury, high-end feel.

Secondary Accents: Muted cream or "off-white" for text and fine-line details. This creates a high-contrast but "soft" look that feels relaxing rather than aggressive.

Aesthetic Goal: It should look like a mobile spa or a high-end boutique cleaning company. No "bubbles," "sparkles," or typical cleaning icons.

Key Information (The Essentials)
The Tagline: "Your Home, Reset." (Placed elegantly under the side logos or on the rear quarter panels).

Phone Number: 7415 000

Socials/Web: @tidalhousekeepco | tidalhousekeepco.com.au

Somewhere small so not to disrupt the design: A Brennick Group Signature Service maybe with the Brennick Group logo.

Require the print ready and AI files.

```html
<!DOCTYPE html>
<html lang="en">
<head>
<meta charset="utf-8">
<title>Tidal Housekeep Co. – Vorex Malden Side Wrap</title>
<link rel="stylesheet" href="https://fonts.googleapis.com/css2?family=Cormorant+Garamond:wght@400&family=Oswald:wght@500;700&display=swap">
<style>
  :root {
    --page: #eceae6;
    --wrap-base: #2e2c25;
    --wrap-shade: #24231e;
    --wrap-text: #9aaba6;
    --wrap-text-soft: #8c9c97;
    --seam: #1c1b17;
  }
  * { margin: 0; padding: 0; box-sizing: border-box; }
  html, body {
    width: 1200px;
    height: 1200px;
    overflow: hidden;
    background: var(--page);
  }
  .canvas {
    position: relative;
    width: 1200px;
    height: 1200px;
    display: flex;
    align-items: center;
    justify-content: center;
  }
  .wrap-panel {
    position: relative;
    width: 1080px;
    height: 440px;
    border-radius: 28px;
    background: linear-gradient(180deg, var(--wrap-base) 0%, var(--wrap-shade) 100%);
    overflow: hidden;
  }
  .door-seam {
    position: absolute;
    left: 560px;
    top: 0;
    width: 2px;
    height: 100%;
    background: var(--seam);
  }
  .front-door {
    position: absolute;
    left: 70px;
    top: 110px;
    width: 460px;
  }
  .brand-name {
    font-family: "Cormorant Garamond", serif;
    font-weight: 400;
    font-size: 50px;
    letter-spacing: 2px;
    color: var(--wrap-text);
    white-space: nowrap;
  }
  .contact-row {
    margin-top: 70px;
    display: flex;
    align-items: baseline;
    gap: 34px;
  }
  .phone {
    font-family: "Oswald", sans-serif;
    font-weight: 700;
    font-size: 44px;
    letter-spacing: 3px;
    color: var(--wrap-text);
  }
  .handle {
    font-family: "Oswald", sans-serif;
    font-weight: 500;
    font-size: 17px;
    letter-spacing: 1px;
    color: var(--wrap-text-soft);
  }
  .rear-door {
    position: absolute;
    left: 610px;
    top: 110px;
    width: 420px;
  }
  .tagline {
    font-family: "Oswald", sans-serif;
    font-weight: 700;
    color: var(--wrap-text);
    line-height: 1;
    text-transform: uppercase;
  }
  .tagline-top {
    display: block;
    font-size: 54px;
    letter-spacing: 1px;
  }
  .tagline-bottom {
    display: block;
    margin-top: 6px;
    font-size: 84px;
    letter-spacing: 2px;
  }
  .website {
    margin-top: 52px;
    font-family: "Oswald", sans-serif;
    font-weight: 500;
    font-size: 17px;
    letter-spacing: 1px;
    color: var(--wrap-text-soft);
    text-transform: uppercase;
  }
</style>
</head>
<body>
  <main class="canvas">
    <section class="wrap-panel" aria-label="Vorex Malden side wrap layout">
      <div class="door-seam"></div>

      <div class="front-door">
        <div class="brand-name">Tidal Housekeep Co.</div>
        <div class="contact-row">
          <span class="phone">7415 000</span>
          <span class="handle">@TIDALHOUSEKEEPCO</span>
        </div>
      </div>

      <div class="rear-door">
        <h1 class="tagline">
          <span class="tagline-top">Your Home,</span>
          <span class="tagline-bottom">Reset.</span>
        </h1>
        <div class="website">tidalhousekeepco.com.au</div>
      </div>
    </section>
  </main>
</body>
</html>
```